VELMIT Business Card

VELMIT (www.velmitpools.example) is a veteran in the swimming pool maintenance and repair business..we have served our clients for 15 years and have a research chemist, an electrician, a plumber and a pool building contractor (in part) on staff...We want to provide a business card that has a dual purpose, that people want to keep around, that leaves people speechless in the sense that they understand the mission of and the experience level of the TEAM at VELMIT.

Target Market(s)

persons who enjoy swimming and make it a priority to swim

Industry/Entity Type

Building

Font styles to use
Serif
Sans Serif

Colors
85acd3
3176b5
95b6d8
3276b5
0355a3
0555a3
0255a3
0455a3
85abd2

Requirements
Must have
• name, title, address, email, text
Nice to have
• a die cut shape
Should not have
• cartoons, pictures of pools

```html
<!DOCTYPE html>
<html lang="en">
<head>
<meta charset="utf-8">
<title>VELMIT Business Card</title>
<link rel="stylesheet" href="https://fonts.googleapis.com/css2?family=Roboto:wght@400;500;700&display=swap">
<style>
  :root {
    --stage: #2b2827;
    --card-light: #49b0dc;
    --card-mid: #3a9fcb;
    --card-deep: #2f8dba;
    --wave: rgba(20, 90, 140, 0.18);
    --white: #ffffff;
    --brand-blue: #3276b5;
    --icon-blue: #3a9fcb;
  }
  * { box-sizing: border-box; margin: 0; padding: 0; }
  html, body {
    width: 1200px;
    height: 1000px;
    overflow: hidden;
    background: var(--stage);
    font-family: "Roboto", Arial, sans-serif;
  }
  .canvas { position: relative; width: 1200px; height: 1000px; }

  .card {
    position: absolute;
    width: 800px;
    height: 420px;
    border-radius: 170px 0 170px 0;
    overflow: hidden;
    color: var(--white);
    background:
      radial-gradient(ellipse at 30% 10%, var(--card-light) 0%, transparent 60%),
      linear-gradient(160deg, var(--card-mid) 0%, var(--card-deep) 100%);
  }
  .card-wave {
    position: absolute;
    right: 0; top: 0;
    width: 55%; height: 100%;
    background: linear-gradient(120deg, transparent 20%, var(--wave) 55%, transparent 90%);
  }

  /* Back side: service promises */
  .card-back { left: 360px; top: 40px; }
  .promise-list {
    position: absolute;
    left: 150px; top: 90px;
    list-style: none;
  }
  .promise-list li {
    position: relative;
    padding-left: 32px;
    margin-bottom: 20px;
    font-weight: 700;
    font-size: 22px;
    letter-spacing: 0.5px;
    text-transform: uppercase;
  }
  .promise-list li::before {
    content: "";
    position: absolute;
    left: 0; top: 7px;
    width: 10px; height: 10px;
    border-radius: 50%;
    background: var(--white);
  }

  /* Front side: identity and contact */
  .card-front { left: 50px; top: 520px; height: 440px; }
  .brand-disc {
    position: absolute;
    left: 60px; top: 110px;
    width: 250px; height: 250px;
    border-radius: 50%;
    background: var(--white);
    display: flex;
    align-items: center;
    justify-content: center;
  }
  .brand-name {
    font-weight: 500;
    font-size: 48px;
    letter-spacing: 2px;
    color: var(--brand-blue);
  }
  .person {
    position: absolute;
    left: 360px; top: 50px;
  }
  .person-name { font-weight: 700; font-size: 28px; }
  .person-title { font-weight: 400; font-size: 19px; margin-top: 4px; }
  .contact-list {
    position: absolute;
    left: 360px; top: 170px;
    list-style: none;
  }
  .contact-list li {
    display: flex;
    align-items: flex-start;
    gap: 18px;
    font-size: 18px;
    line-height: 1.25;
    margin-bottom: 10px;
  }
  .contact-icon {
    flex: none;
    width: 22px; height: 22px;
    border-radius: 50%;
    background: var(--white);
    display: flex;
    align-items: center;
    justify-content: center;
  }
  .contact-icon svg { width: 13px; height: 13px; fill: var(--icon-blue); }
</style>
</head>
<body>
<main class="canvas">

  <section class="card card-back" aria-label="Card back">
    <div class="card-wave" role="img" aria-label="Soft water wave pattern"></div>
    <ul class="promise-list">
      <li>Clean clear &amp; blue water</li>
      <li>Smooth &amp; clean tiles</li>
      <li>No more strong odors</li>
      <li>Latest cleaning equipment</li>
    </ul>
  </section>

  <section class="card card-front" aria-label="Card front">
    <div class="card-wave" role="img" aria-label="Soft water wave pattern"></div>
    <div class="brand-disc"><span class="brand-name">VELMIT</span></div>
    <div class="person">
      <div class="person-name">Loren Ipsum</div>
      <div class="person-title">Director</div>
    </div>
    <ul class="contact-list">
      <li>
        <span class="contact-icon"><svg viewBox="0 0 24 24"><path d="M6.6 10.8c1.4 2.8 3.8 5.1 6.6 6.6l2.2-2.2c.3-.3.7-.4 1-.2 1.1.4 2.3.6 3.6.6.6 0 1 .4 1 1V20c0 .6-.4 1-1 1C10.6 21 3 13.4 3 4c0-.6.4-1 1-1h3.5c.6 0 1 .4 1 1 0 1.3.2 2.5.6 3.6.1.3 0 .7-.2 1l-2.3 2.2z"/></svg></span>
        <span>+91 5550 123 456</span>
      </li>
      <li>
        <span class="contact-icon"><svg viewBox="0 0 24 24"><path d="M2 5h20v14H2z M2 5l10 8 10-8" /></svg></span>
        <span>hello@velmitpools.example</span>
      </li>
      <li>
        <span class="contact-icon"><svg viewBox="0 0 24 24"><path d="M12 2a10 10 0 100 20 10 10 0 000-20zm0 2c1 1.3 1.8 3.5 2 6h-4c.2-2.5 1-4.7 2-6zm-4 8h8c-.2 2.5-1 4.7-2 6h-4c-1-1.3-1.8-3.5-2-6zM4 12h2c0 2 .5 4 1.3 5.6A8 8 0 014 12zm16 0a8 8 0 01-3.3 5.6c.8-1.6 1.3-3.6 1.3-5.6h2z"/></svg></span>
        <span>www.velmitpools.example</span>
      </li>
      <li>
        <span class="contact-icon"><svg viewBox="0 0 24 24"><path d="M12 2a7 7 0 00-7 7c0 5 7 13 7 13s7-8 7-13a7 7 0 00-7-7zm0 9.5A2.5 2.5 0 1112 6.5a2.5 2.5 0 010 5z"/></svg></span>
        <span>Lorem Ipsum,Dummy text<br>Printing, Typesetting<br>Industry 123 456</span>
      </li>
    </ul>
  </section>

</main>
</body>
</html>
```